Recruitment Agency in Texas, needs a stand out header letter

Our colours are red and grey and can be found on our website
just my logo will be sufficient and address...

Target Market(s)

Engineering Manufacturing

Colors
0094D4
00A9DD
6FCCEA
C7EBF8
E9F6FB
EB3D1F
EC4F4E
F09395
F8D3D4
FCEDEE

Requirements
Must have
• use colors red and grey
Should not have
• Please use same colors and font as my logo. My website is kelbrantstaffing.net

```html
<!DOCTYPE html>
<html lang="en">
<head>
<meta charset="utf-8">
<title>Kelbrant Staffing Letterhead</title>
<link href="https://fonts.googleapis.com/css2?family=Roboto:wght@300;400;500&family=Great+Vibes&display=swap" rel="stylesheet">
<style>
  :root {
    --bg: #e6e6e6;
    --paper: #f3f3f3;
    --red: #dc1f26;
    --grey: #5e5f62;
    --grey-bar: #a3a3a3;
    --ink: #2b2b2b;
    --muted: #555659;
  }
  * { margin: 0; padding: 0; box-sizing: border-box; }
  html, body { width: 1200px; height: 1200px; overflow: hidden; background: var(--bg); }
  body { font-family: "Roboto", sans-serif; position: relative; }
  .letterhead {
    position: absolute; left: 200px; top: 34px; width: 800px; height: 1132px;
    background: var(--paper); overflow: hidden;
  }
  .side-bar { position: absolute; left: 0; top: 49px; width: 10px; height: 81px; background: var(--grey-bar); }
  .office {
    position: absolute; left: 59px; top: 45px; font-weight: 300; font-size: 12.5px;
    line-height: 16px; color: var(--muted);
  }
  .office .contact { margin-top: 6px; }
  .contact-line { display: flex; align-items: center; gap: 5px; }
  .contact-line svg { width: 10px; height: 10px; }
  .brand {
    position: absolute; right: 84px; top: 72px; font-weight: 500; font-size: 31px;
    letter-spacing: -0.5px; color: var(--red);
  }
  .letter-body {
    position: absolute; left: 85px; top: 262px; width: 629px; font-weight: 300;
    font-size: 13px; line-height: 18.8px; color: var(--ink);
  }
  .date { margin-bottom: 19px; }
  .recipient { margin-bottom: 37px; }
  .salutation { margin-bottom: 19px; }
  .letter-body p.para { text-align: justify; margin-bottom: 18.8px; }
  .closing { margin-top: 38px; }
  .signature { font-family: "Great Vibes", cursive; font-size: 27px; line-height: 34px; margin-left: 4px; color: var(--ink); }
  .footer-art { position: absolute; left: 0; top: 0; }
  .web {
    position: absolute; right: 84px; bottom: 16px; font-size: 13px; font-weight: 300; color: #fff;
  }
</style>
</head>
<body>
<main class="letterhead">
  <div class="side-bar"></div>

  <address class="office" style="font-style:normal">
    <div>Central Houston Office</div>
    <div>48 Larkfield Plaza Suite 900</div>
    <div>Houston, TX 77057</div>
    <div class="contact">
      <div class="contact-line">
        <svg viewBox="0 0 10 10" aria-hidden="true"><path d="M2 1 L4 3 L3 4 Q4 6 6 7 L7 6 L9 8 L8 9 Q3 9 1 2 Z" fill="var(--red)"/></svg>
        <span>(+1) 832-555-0187</span>
      </div>
      <div class="contact-line">
        <svg viewBox="0 0 10 10" aria-hidden="true"><rect x="0.5" y="2" width="9" height="6" fill="var(--red)"/><path d="M0.5 2 L5 5.5 L9.5 2" stroke="#fff" stroke-width="0.9" fill="none"/></svg>
        <span>info@kelbrantstaffing.net</span>
      </div>
    </div>
  </address>

  <div class="brand">KelbrantStaffing</div>

  <section class="letter-body">
    <p class="date">01 January 2050</p>
    <p class="recipient">Company (Pvt) Ltd.<br>PO Box 3355 Mainville St<br>Sample City Country 3355</p>
    <p class="salutation">Dear Daniel Hartwell,</p>
    <p class="para">Lorem ipsum dolor sit amet, consectetuer adipiscing elit, sed diam nonummy nibh euismod tincidunt ut laoreet dolore magna aliquam erat volutpat. Ut wisi enim ad minim veniam, quis nostrud exerci tation ullamcorper suscipit lobortis nisl ut aliquip ex ea commodo consequat. Duis dolore te feugait nulla facilisi. Nam liber tempor cum soluta nobis eleifend option congue nihil imperdiet doming id quod mazim placerat facer possim assum. Lorem ipsum dolor sit amet, consectetuer adipiscing elit, sed diam nonummy nibh euismod tincidunt ut laoreet dolore magna aliquam erat volutpat. Ut wisi enim ad minim veniam, quis nostrud exerci tation ullamcorper suscipit lobortis nisl ut aliquip ex ea commodo consequat.</p>
    <p class="para">Consectetuer adipiscing elit, sed diam nonummy nibh euismod tincidunt ut laoreet dolore magna aliquam erat volutpat. Ut wisi enim ad minim veniam, quis nostrud exerci tation ullamcorper suscipit lobortis nisl ut aliquip ex ea commodo consequat. Consectetuer adipiscing elit, sed diam nonummy nibh euismod tincidunt ut laoreet dolore magna aliquam erat volutpat. Ut wisi enim ad minim veniam, quis nostrud exerci tation ullamcorper suscipit lobortis nisl ut aliquip ex ea commodo consequat.</p>
    <p class="para">Consectetuer adipiscing elit, sed diam nonummy nibh euismod tincidunt ut laoreet dolore magna aliquam erat volutpat. Ut wisi enim ad minim veniam, quis nostrud exerci tation ullamcorper suscipit lobortis nisl ut aliquip ex ea commodo consequat. Consectetuer adipiscing elit, sed diam nonummy nibh euismod tincidunt ut laoreet dolore magna aliquam erat volutpat. Ut wisi enim ad minim veniam, quis nostrud exerci tation ullamcorper suscipit lobortis nisl ut aliquip ex ea commodo consequat.</p>
    <p class="closing">Sincerely Yours</p>
    <p class="signature">Owen Carraway</p>
  </section>

  <svg class="footer-art" width="800" height="1132" viewBox="0 0 800 1132" aria-hidden="true">
    <path d="M141 1132 Q420 1056 800 1078 L800 1082 Q470 1066 230 1132 Z" fill="var(--grey)"/>
    <path d="M244 1132 Q500 1078 800 1091 L800 1132 Z" fill="var(--red)"/>
  </svg>
  <div class="web">www.kelbrantstaffing.net</div>
</main>
</body>
</html>
```